Landscape design build company door flyer

I would like this flyer to convey a high-level of professionalism for a company that is excellent with communication with their clients as well as a company that does incredible installations

Went on vacation/holiday

```html
<!DOCTYPE html>
<html lang="en">
<head>
<meta charset="UTF-8">
<title>Summit Stone Builders – Premium Paver Installation</title>
<link rel="stylesheet" href="https://fonts.googleapis.com/css2?family=Bebas+Neue&family=Rubik:wght@500;600;700&display=swap">
<style>
  :root {
    --navy: #1c3441;
    --paper: #e6e6e6;
    --white: #ffffff;
    --sky: #8fb6d8;
    --wood: #b07a4a;
    --stone: #6f6d6a;
    --leaf: #5d6b3e;
  }
  * { margin: 0; padding: 0; box-sizing: border-box; }
  html, body { width: 1200px; height: 3106px; overflow: hidden; }
  body { background: var(--paper); font-family: "Rubik", sans-serif; color: var(--navy); }
  .flyer { position: relative; width: 1200px; height: 3106px; overflow: hidden; background: var(--paper); }

  .hero { position: absolute; left: 0; top: 0; width: 1200px; height: 940px; }

  .brand-badge {
    position: absolute; left: 56px; top: 66px; width: 280px; height: 280px;
    border-radius: 50%; background: var(--white);
    display: flex; align-items: center; justify-content: center; text-align: center;
  }
  .brand-name { font-weight: 600; font-size: 27px; line-height: 1.2; color: var(--navy); }

  .headline {
    position: absolute; left: 0; top: 1042px; width: 1200px; text-align: center;
    font-family: "Bebas Neue", sans-serif; font-size: 128px; line-height: 116px; color: var(--navy);
  }

  .photo-ring { position: absolute; border-radius: 50%; border: 11px solid var(--navy); }
  .photo-ring.patio { left: 37px; top: 1515px; width: 390px; height: 390px;
    background: linear-gradient(180deg, #b9cce0 0%, #b5814f 30%, #7a6f63 60%, #6f7a48 100%); }
  .photo-ring.covered-deck { left: 52px; top: 1988px; width: 476px; height: 476px;
    background: linear-gradient(180deg, #9fc0df 0%, #a7764a 28%, #3e4650 58%, #8d8a83 80%, #6d7d45 100%); }
  .photo-ring.stair-deck { left: 488px; top: 2306px; width: 566px; height: 566px;
    background: linear-gradient(180deg, #c4d4e4 0%, #2f4a64 35%, #5a5550 65%, #6b6a50 100%); }

  .intro {
    position: absolute; left: 498px; top: 1526px; width: 600px;
    font-weight: 500; font-size: 37px; line-height: 55px; text-align: justify;
    text-align-last: center; hyphens: manual;
  }

  .cta {
    position: absolute; left: 593px; top: 2128px; width: 607px; height: 108px;
    background: var(--navy); color: var(--white);
    font-weight: 700; font-size: 41px; line-height: 108px; padding-left: 34px;
  }

  .subhead {
    position: absolute; left: 62px; top: 2582px; width: 400px;
    font-weight: 700; font-size: 48px; line-height: 62px;
  }

  .footer {
    position: absolute; left: 0; top: 2940px; width: 1200px; height: 166px;
    background: var(--navy); color: var(--white); font-family: "Bebas Neue", sans-serif;
  }
  .footer .call-label { position: absolute; left: 62px; top: 34px; font-size: 44px; line-height: 1; }
  .footer .phone { position: absolute; left: 58px; top: 80px; font-size: 76px; line-height: 1; }
  .footer .website { position: absolute; right: 52px; top: 92px; font-size: 44px; line-height: 1; }
</style>
</head>
<body>
<main class="flyer">
  <svg class="hero" viewBox="0 0 1200 940" xmlns="http://www.w3.org/2000/svg">
    <defs>
      <linearGradient id="heroTones" x1="0" y1="0" x2="0" y2="1">
        <stop offset="0" stop-color="#7fa8d4"/>
        <stop offset="0.22" stop-color="#b9854f"/>
        <stop offset="0.45" stop-color="#3a3d3f"/>
        <stop offset="0.7" stop-color="#77736c"/>
        <stop offset="1" stop-color="#5e5a55"/>
      </linearGradient>
    </defs>
    <path role="img" aria-label="Covered outdoor living pavilion with stone fireplace, bar counter and timber beams"
          fill="url(#heroTones)"
          d="M0,0 H1200 V522 C1050,560 930,640 760,742 C600,830 430,845 270,800 C160,770 70,740 0,706 Z"/>
    <path class="wave" fill="var(--navy)"
          d="M0,706 C70,740 160,770 270,800 C430,845 600,830 760,742 C930,640 1050,560 1200,522 V722 C1020,720 900,760 720,840 C560,910 400,935 250,880 C150,845 60,790 0,740 Z"/>
  </svg>

  <div class="brand-badge"><span class="brand-name">SUMMIT STONE<br>BUILDERS</span></div>

  <h1 class="headline">Elevate Your Driveway<br>with a Premium Paver<br>Installation</h1>

  <div class="photo-ring patio" role="img" aria-label="Timber-framed patio cover over a stone outdoor kitchen"></div>
  <p class="intro">Introducing the perfect en&shy;hancement for your home exte&shy;rior: an expertly crafted paver driveway. If you’re interested in elevating the curb appeal of your property with a touch of el&shy;egance and sophistication that only a paver driveway can bring, then keep reading!</p>

  <div class="photo-ring covered-deck" role="img" aria-label="Covered patio with cedar posts, lounge seating and paver floor"></div>
  <div class="cta">GET A FREE ESTIMATE</div>

  <div class="photo-ring stair-deck" role="img" aria-label="Elevated deck with black railings and stairs beside a blue house"></div>
  <h2 class="subhead">It’s Time to Enhance Your Home Curb Appeal and</h2>

  <footer class="footer">
    <div class="call-label">Call Us Now</div>
    <div class="phone">(206) 555-0148</div>
    <div class="website">www.summitstonebuilders.com</div>
  </footer>
</main>
</body>
</html>
```